Business Card Design Project

KRV Management Consulting, LLC is a management consulting firm focused on improving an organization’s health and wellness while enhancing company performance with an emphasis on winning in the marketplace, profitable growth, team building, culture enablement and innovation.

Industry/Entity Type

Business

```html
<!DOCTYPE html>
<html lang="en">
<head>
<meta charset="utf-8">
<title>KRV Management Consulting, LLC — Business Card</title>
<link rel="stylesheet" href="https://fonts.googleapis.com/css2?family=Libre+Baskerville:wght@400&display=swap">
<style>
  :root {
    --page-bg: #e4e5e7;
    --card-bg: #1d1d1d;
    --card-sheen: #3a3a3a;
    --text-light: #f2f2f2;
    --accent-green: #6cb33f;
  }
  * { margin: 0; padding: 0; box-sizing: border-box; }
  html, body {
    width: 1200px; height: 869px; overflow: hidden;
    background: var(--page-bg);
  }
  .sheet {
    width: 1200px; height: 869px;
    display: flex; flex-direction: column;
    align-items: center; justify-content: center; gap: 40px;
  }
  .card {
    position: relative;
    width: 660px; height: 377px;
    border-radius: 30px;
    background: linear-gradient(100deg, var(--card-bg) 0%, var(--card-bg) 22%, var(--card-sheen) 36%, var(--card-bg) 52%, var(--card-bg) 100%);
    box-shadow: 0 10px 24px rgba(0,0,0,0.18);
    font-family: 'Libre Baskerville', Georgia, serif;
    font-weight: 400;
    color: var(--text-light);
  }
  .firm-name {
    position: absolute;
    display: flex; align-items: center; gap: 14px;
    font-size: 20px; font-weight: 400; line-height: 1.35;
    color: var(--text-light);
  }
  .firm-name .marker {
    width: 12px; height: 12px; flex: none;
    background: var(--accent-green);
  }
  .card--back .firm-name {
    left: 50%; top: 50%; transform: translate(-50%, -50%);
    white-space: nowrap;
  }
  .card--front .firm-name {
    left: 400px; top: 142px; width: 220px;
  }
  .holder-name {
    position: absolute; left: 50px; top: 78px;
    font-size: 26px; font-weight: 400; letter-spacing: 0.5px;
  }
  .contact-list {
    position: absolute; left: 56px; top: 140px;
    list-style: none;
  }
  .contact-list li {
    display: flex; align-items: center; gap: 16px;
    font-size: 15px; height: 30px;
  }
  .contact-list svg { width: 16px; height: 16px; fill: var(--accent-green); flex: none; }
  .divider {
    position: absolute; left: 372px; top: 116px;
    width: 3px; height: 116px;
    background: var(--accent-green);
  }
</style>
</head>
<body>
<main class="sheet">
  <section class="card card--back" aria-label="Card back">
    <p class="firm-name"><span class="marker" aria-hidden="true"></span><span>KRV Management Consulting, LLC</span></p>
  </section>

  <section class="card card--front" aria-label="Card front">
    <h1 class="holder-name">Name Here</h1>
    <ul class="contact-list">
      <li>
        <svg viewBox="0 0 24 24" aria-hidden="true"><path d="M6.6 10.8a15 15 0 0 0 6.6 6.6l2.2-2.2c.3-.3.7-.4 1-.2 1.1.4 2.3.6 3.6.6.6 0 1 .4 1 1V20c0 .6-.4 1-1 1A17 17 0 0 1 3 4c0-.6.4-1 1-1h3.5c.6 0 1 .4 1 1 0 1.3.2 2.5.6 3.6.1.3 0 .7-.2 1z"/></svg>
        <span>phone number</span>
      </li>
      <li>
        <svg viewBox="0 0 24 24" aria-hidden="true"><path d="M2 5h20v14H2z"/><path d="M2 5l10 8 10-8v1.6l-10 8-10-8z" fill="#1d1d1d"/></svg>
        <span>email here</span>
      </li>
      <li>
        <svg viewBox="0 0 24 24" aria-hidden="true"><path d="M12 2a10 10 0 1 0 0 20 10 10 0 0 0 0-20zm6.9 6h-3a15 15 0 0 0-1.3-3.9A8 8 0 0 1 18.9 8zM12 4c.8 1.2 1.5 2.5 1.9 4h-3.8c.4-1.5 1.1-2.8 1.9-4zM4.3 14a8 8 0 0 1 0-4h3.4a16 16 0 0 0 0 4zm.8 2h3a15 15 0 0 0 1.3 3.9A8 8 0 0 1 5.1 16zm3-8h-3a8 8 0 0 1 4.3-3.9C8.8 5.3 8.4 6.6 8.1 8zM12 20c-.8-1.2-1.5-2.5-1.9-4h3.8c-.4 1.5-1.1 2.8-1.9 4zm2.3-6H9.7a14 14 0 0 1 0-4h4.6a14 14 0 0 1 0 4zm.3 5.9c.6-1.2 1-2.5 1.3-3.9h3a8 8 0 0 1-4.3 3.9zm1.7-5.9a16 16 0 0 0 0-4h3.4a8 8 0 0 1 0 4z"/></svg>
        <span>website here</span>
      </li>
      <li>
        <svg viewBox="0 0 24 24" aria-hidden="true"><path d="M12 2a7 7 0 0 0-7 7c0 5.2 7 13 7 13s7-7.8 7-13a7 7 0 0 0-7-7zm0 9.5a2.5 2.5 0 1 1 0-5 2.5 2.5 0 0 1 0 5z"/></svg>
        <span>address</span>
      </li>
    </ul>
    <div class="divider" aria-hidden="true"></div>
    <p class="firm-name"><span>KRV Management Consulting, LLC</span></p>
  </section>
</main>
</body>
</html>
```